Young, funky marketing collateral and other stuff
Exciting and innovative ideas welcomed
We are thrilled with the designs that have come in and are now spoilt for choice as they are all individually very good. We appreciate the trouble you have gone to in response to our direct feedback as we 'fine tune' our ideas. Thanks designers, you are all great.
A big thank you also to Owen in Support who has helped to smooth the way between us and the designers when we have run into difficulty conveying some of our ideas.
Have already recommended Tallowspan to others
Regards
RTolley
Fernwick logo
#14: the way that the fernwick logo colours have been made neutral is very good and perfectly acceptable to us.
A general reminder; fernwick logo only on biz card, folder, letterhead and signature. Not on other things.
Address Label:
#13 has the right idea for the address label, however we would like it to be landscape design rather than portrait
Yard signs: it would be good to have the branding colours 'frame' the signs in some way too thanks. Thanks for your great efforts.
Hi Designers
On the yard signs, please include as part of the branding template:
www.kvtp.co.nz
Thanks
Clarification on Registry. Please use the following 'Open for Inspection Registry' not 'Open House Registry'. Thanks.
Also, the Registry does not require fernwick logo.
Brightnook, thanks for your ideas. #4 is attractive, we prefer the way you have presented the company address in the letterhead, by contrast in #3 the company address in footer looks a bit staggered and not so smart. The logo reflection on the #4 folder is also very appealing.
#5 Thank you for your new design.
The address label; please make the dot dot lines in the receiver's address longer and more central. We will be handwriting the receiver's address on the dot dot line and it needs to have enough space to do this and so that a courier or post office can read the address and deliver the package easily.
Thanks for the new designs. I can see that trying to incorporate the 2nd logo (fernwick property) is simply going to cause confusion however we do need somehow to represent the second company. Instead of using logo, please just use company name and designation which is 'Fernwick Property Ltd, Licensed Agent (PLNB) 2008. Please include this on the business card, folder, letterhead, and signature. It would be suitable to have it, for instance, in the bottom line of the footer, the two company names as bullet points.
@DW - please check your private message on top right corner after clicking messages once you log in. Thanks
A big thanks to pixvellor for starting of the process with neat designs #1 and #2.
My brief may not have been totally clear so here are a couple more thoughts:
The mailing label: There needs to be a space (........... line) after 'company/name etc so that the sender can hand write the details in. For example:
Company/Name ...........................................
Address .................................................
.........................................................City ....................................................
Phone ...................................................
Attention ...............................................
Please also note my comment at start of brief about also including Fernwick property details on some of the collateral. If it's going to look too crowded, just use the fernwick logo.
On the 'inspect today' sign, the 'inspect today' plus arrow are major components, the branding is minor. This sign will be placed at intersections directing buyers to a home, so the size of the arrow is important.
Thanks everyone and we look forward to seeing your ideas.

```html
<!DOCTYPE html>
<html lang="en">
<head>
<meta charset="utf-8">
<title>Yard Sign – Section 36 Land Listing</title>
<link rel="stylesheet" href="https://fonts.googleapis.com/css2?family=Arimo:ital,wght@0,400;0,700;1,700&display=swap">
<style>
  :root {
    --blue-deep: #0b4c9f;
    --blue-main: #1d6fd2;
    --blue-light: #5db0ee;
    --white: #ffffff;
    --frame: #d9dde2;
    --photo-sky: #6f9fc9;
    --photo-house: #c9c3b4;
    --photo-garden: #5f8a3a;
    --stage: #eef1f4;
  }
  * { margin: 0; padding: 0; box-sizing: border-box; }
  html, body {
    width: 1200px;
    height: 814px;
    overflow: hidden;
    background: var(--stage);
    font-family: "Arimo", Arial, sans-serif;
  }
  .yard-sign {
    position: relative;
    width: 1200px;
    height: 814px;
    border: 8px solid var(--frame);
    background: var(--blue-main);
    overflow: hidden;
  }
  .property-photo {
    position: absolute;
    top: 120px; left: 0;
    width: 100%;
    height: 560px;
    background:
      linear-gradient(180deg, transparent 55%, var(--photo-garden) 100%),
      radial-gradient(ellipse 40% 45% at 55% 48%, var(--photo-house) 0%, var(--photo-house) 60%, transparent 100%),
      linear-gradient(180deg, var(--photo-sky) 0%, #a8c6df 60%, var(--photo-garden) 100%);
  }
  .sign-waves {
    position: absolute;
    left: 0; top: 0;
    width: 1184px;
    height: 798px;
  }
  .legal-description {
    position: absolute;
    top: 46px; left: 0;
    width: 100%;
    text-align: center;
    color: var(--white);
    font-weight: 700;
    font-style: italic;
    font-size: 36px;
    white-space: nowrap;
  }
  .agency-badge {
    position: absolute;
    top: 215px; left: 70px;
    width: 370px;
    height: 90px;
    border-radius: 45px;
    background: var(--white);
    border: 5px solid var(--blue-light);
    display: flex;
    align-items: center;
    justify-content: center;
    gap: 14px;
    color: var(--blue-deep);
    font-weight: 700;
    font-size: 34px;
  }
  .agency-badge .mark {
    width: 34px; height: 34px;
    background: var(--blue-main);
  }
  .property-details {
    position: absolute;
    left: 55px; top: 690px;
    color: var(--white);
    font-weight: 700;
    font-size: 33px;
    line-height: 38px;
  }
  .web-address {
    position: absolute;
    left: 820px; top: 680px;
    width: 270px;
    height: 96px;
    border-radius: 50%;
    background: var(--white);
    display: flex;
    align-items: center;
    justify-content: center;
    color: var(--blue-deep);
    font-weight: 700;
    font-size: 26px;
    white-space: nowrap;
  }
</style>
</head>
<body>
  <div class="yard-sign">
    <div class="property-photo" role="img" aria-label="Photograph of a two-storey family home with a front veranda, garden beds and trees"></div>

    <svg class="sign-waves" viewBox="0 0 1184 798" aria-hidden="true">
      <path d="M0 0 H1184 V120 C950 175 700 110 430 150 C260 175 110 165 0 140 Z" fill="var(--blue-main)"/>
      <path d="M0 140 C110 165 260 175 430 150 C700 110 950 175 1184 120 V135 C950 195 700 128 430 168 C260 190 110 182 0 160 Z" fill="var(--blue-light)"/>
      <path d="M0 640 C220 600 460 700 720 655 C930 620 1080 600 1184 615 V798 H0 Z" fill="var(--blue-light)"/>
      <path d="M0 660 C220 625 460 720 720 675 C930 640 1080 625 1184 640 V798 H0 Z" fill="var(--blue-main)"/>
      <path d="M0 780 C300 760 700 800 1184 770 V798 H0 Z" fill="var(--blue-deep)"/>
    </svg>

    <p class="legal-description">NE NE Section 36, Township 40, Range 40 East W.M. 40 acres)</p>

    <div class="agency-badge"><span class="mark"></span>Kovatra Realty</div>

    <p class="property-details">Property discription, Property discription<br>Property discription</p>

    <div class="web-address">www.kvtp.co.nz</div>
  </div>
</body>
</html>
```